Ordnerdesign für Experte für Versicherungs - und Haftungsfragen im Etiketten - und Verpackungsdruck
Ordnerdesign für Experte für Versicherungs - und Haftungsfragen im Etiketten - und Verpackungsdr..
Zielgruppe
Ich bin Henrik Wallmoser Experte für Versicherungs - und Haftungsfragen im Etiketten - und Verpackungsdruck (meine CI Farben sind orange /schwarz ) Meine Company und das Produkt ist die tarvolink und der tarvolnk Schutzbrief für Druckerereien (schwarz/gelb)
Aufgabenstellung
Gesucht wird für mein/unser Projekt : Ordnerdesign PLUS Register eines Notfallhandbuchs für Unternehmer . Es gibt zwei Produktlinien - zu beiden ist jeweils der Farbfächer /Broschüre beigefügt : Entweder der Notfallordner soll unter ' Henrik Wallmoser Experte für Haftungsfragen .. ( Orange Schwarz oder die Farben meiner Company ( tarvolink Schwarz - gelb ) siehe Broschüre angelegt werden. freie Hand , was also besser passt .

```html
<!DOCTYPE html>
<html lang="de">
<head>
<meta charset="utf-8">
<title>Notfallhandbuch – Ordner und Register</title>
<link href="https://fonts.googleapis.com/css2?family=Archivo:wght@400;600;800&family=Poppins:wght@500;600;700&display=swap" rel="stylesheet">
<style>
  :root {
    --bg: #f4f4f6;
    --red: #e2472f;
    --red-deep: #c8322a;
    --red-pattern: rgba(190, 30, 45, 0.35);
    --yellow: #f1c12b;
    --white: #ffffff;
    --ink: #1d1d1d;
    --sign: #3f7f73;
  }
  * { box-sizing: border-box; margin: 0; padding: 0; }
  html, body { width: 1200px; height: 889px; overflow: hidden; background: var(--bg); }
  body { font-family: "Archivo", sans-serif; position: relative; }

  /* Cover */
  .cover {
    position: absolute; left: 50px; top: 130px; width: 560px; height: 640px;
    background: linear-gradient(160deg, #ea5a3c 0%, var(--red) 45%, var(--red-deep) 100%);
    overflow: hidden;
  }
  .cover__pattern {
    position: absolute; left: 200px; top: 20px; width: 360px; height: 620px;
    background: linear-gradient(200deg, rgba(200,40,50,0.0) 0%, var(--red-pattern) 60%, rgba(200,40,50,0.15) 100%);
  }
  .brand {
    font-family: "Poppins", sans-serif; font-weight: 600; color: var(--yellow);
    letter-spacing: 0.02em;
  }
  .cover .brand { position: absolute; left: 48px; top: 34px; font-size: 15px; }
  .signature {
    background: linear-gradient(90deg, rgba(63,127,115,0.55), rgba(63,127,115,0.25));
    border-radius: 40px;
  }
  .cover .signature { position: absolute; left: 44px; top: 220px; width: 250px; height: 46px; }
  .cover__title {
    position: absolute; left: 40px; top: 272px; color: var(--white);
    font-weight: 800; font-size: 70px; line-height: 0.96; letter-spacing: 0.005em;
  }
  .cover__spine-name {
    position: absolute; left: 22px; top: 610px; transform: rotate(-90deg); transform-origin: left top;
    font-size: 11px; color: var(--ink); white-space: nowrap;
  }
  .cover__icons { position: absolute; left: 368px; top: 478px; display: flex; gap: 30px; }
  .pill {
    background: var(--yellow); color: var(--ink); border-radius: 999px;
    font-family: "Poppins", sans-serif; font-weight: 600; text-transform: uppercase; letter-spacing: 0.1em;
    white-space: nowrap;
  }
  .cover .pill { position: absolute; right: 36px; top: 560px; font-size: 11px; padding: 10px 22px; }

  /* Register title page */
  .register {
    position: absolute; left: 690px; top: 200px; width: 450px; height: 500px;
    background: var(--red); overflow: hidden;
  }
  .register .brand { position: absolute; left: 40px; top: 30px; font-size: 11px; }
  .register__index { position: absolute; right: 70px; top: 120px; text-align: center; }
  .register__index-rule { position: absolute; right: 100px; top: 128px; width: 60px; height: 1px; background: rgba(255,255,255,0.6); }
  .register__index span { display: block; font-size: 9px; color: var(--ink); margin-top: 4px; }
  .register__title {
    position: absolute; left: 40px; top: 180px; color: var(--white);
    font-weight: 800; font-size: 36px; line-height: 1.0;
  }
  .register .pill { position: absolute; left: 40px; top: 322px; font-size: 6.5px; padding: 6px 12px; }
  .register__footer { position: absolute; left: 40px; top: 440px; display: flex; align-items: center; gap: 6px; }
  .register__footer .signature { width: 44px; height: 12px; border-radius: 8px; }
  .register__footer span { font-size: 7px; color: var(--ink); letter-spacing: 0.08em; text-transform: uppercase; }
  .tab {
    position: absolute; right: 0; width: 40px; display: flex; align-items: center; justify-content: center;
  }
  .tab span {
    transform: rotate(-90deg); white-space: nowrap; font-size: 12px; text-transform: uppercase; letter-spacing: 0.04em;
  }
  .tab span::before { content: "● "; }
  .tab--etiketten { top: 150px; height: 130px; color: var(--yellow); }
  .tab--verpackungen { top: 340px; height: 160px; background: var(--yellow); color: var(--ink); border-radius: 18px 0 0 0; }
</style>
</head>
<body>

<section class="cover">
  <div class="cover__pattern" role="img" aria-label="Großes dekoratives Muster aus überlagerten Buchstabenformen in dunklerem Rot"></div>
  <div class="brand">Tarvolink®</div>
  <div class="signature" role="img" aria-label="Handschriftliche Unterschrift von Henrik Wallmoser"></div>
  <h1 class="cover__title">Experte für<br>Haftungs–<br>fragen</h1>
  <div class="cover__spine-name">Henrik Wallmoser</div>
  <div class="cover__icons">
    <svg width="42" height="42" viewBox="0 0 42 42" fill="none" stroke="#1d1d1d" stroke-width="2" aria-label="Etiketten">
      <path d="M6 10 L14 4 H34 V34 H6 Z"/>
      <path d="M10 38 H38 V8"/>
    </svg>
    <svg width="44" height="44" viewBox="0 0 44 44" fill="none" stroke="#1d1d1d" stroke-width="2" aria-label="Verpackung">
      <path d="M4 14 L22 6 L40 14 L40 32 L22 40 L4 32 Z"/>
      <path d="M4 14 L22 22 L40 14 M22 22 V40 M13 10 L31 18 V24"/>
    </svg>
  </div>
  <div class="pill">Etiketten – und Verpackungsdruck</div>
</section>

<section class="register">
  <div class="brand">Tarvolink®</div>
  <div class="register__index-rule"></div>
  <div class="register__index">
    <svg width="22" height="22" viewBox="0 0 22 22"><circle cx="11" cy="11" r="8" fill="none" stroke="#ffffff" stroke-width="3"/></svg>
    <span>Inhalt</span>
  </div>
  <h2 class="register__title">Notfall–<br>handbuch für<br>Unternehmer</h2>
  <div class="pill">Etiketten – und Verpackungsdruck</div>
  <div class="register__footer">
    <div class="signature" role="img" aria-label="Kleine Unterschrift von Henrik Wallmoser"></div>
    <span>Experte für Haftungsfragen</span>
  </div>
  <div class="tab tab--etiketten"><span>Etiketten</span></div>
  <div class="tab tab--verpackungen"><span>Verpackungen</span></div>
</section>

</body>
</html>
```